Business Card Design Project

I would like to have a project of business card with incorporated attachted logo elements in warm colors like: gold, yellow, brown.
We would like incorporate below information into the design
Name of the Company: Continental Hoop Invitational
Name: Dorian Pelkey
Position: Project Director
e-mail: dorian@hoopinvitational.net
mobile: +65 83147092
website: www.hoopinvitational.net
Address: 47 Marbury Lane, #06-11, Singapore 915274
There is a picture attachted which can be used as a back side of the buisness card - we would like to follow the colors theme on the front card ( with the person contact details) how ever the front card we will prefer with white background but with graphfic elements coming from logo.
Project Deadline Extended
Reason: the project has been launched on 24 of April with deadline by 24 of April by mistakes. Thats why I would like to extend the deadline.
Name: Dorian Pelkey
mobile: +65 83147092

```html
<!DOCTYPE html>
<html lang="en">
<head>
<meta charset="utf-8">
<title>Dorian Pelkey – Business Card</title>
<link rel="stylesheet" href="https://fonts.googleapis.com/css2?family=Open+Sans:wght@400;600&display=swap">
<style>
  :root {
    --page: #ffffff;
    --plum: #361a20;
    --brown: #5e3a22;
    --amber: #9c7a1c;
    --lemon: #dccd0a;
    --gold-text: #f2d313;
    --white-text: #ffffff;
    --mark-ink: #2a2a2a;
  }
  * { margin: 0; padding: 0; box-sizing: border-box; }
  html, body {
    width: 1200px; height: 703px; overflow: hidden;
    background: var(--page);
    font-family: "Open Sans", sans-serif;
  }
  .card {
    position: absolute; left: 22px; top: 27px;
    width: 1156px; height: 656px;
    overflow: hidden; background: var(--plum);
  }
  .card-waves { position: absolute; inset: 0; width: 100%; height: 100%; }
  .details { position: absolute; left: 33px; top: 0; width: 720px; }
  .name {
    position: absolute; top: 46px; white-space: nowrap;
    font-size: 48px; font-weight: 400; color: var(--gold-text);
  }
  .role {
    position: absolute; top: 118px; white-space: nowrap;
    font-size: 38px; color: var(--gold-text);
  }
  .company {
    position: absolute; top: 173px; white-space: nowrap;
    font-size: 40px; color: var(--white-text);
  }
  .rule {
    position: absolute; top: 236px; left: 0; width: 685px; height: 2px;
    background: var(--gold-text);
  }
  .address {
    position: absolute; top: 252px; white-space: nowrap;
    font-size: 36px; line-height: 52px; color: var(--white-text);
  }
  .contacts {
    position: absolute; top: 414px; font-size: 36px; line-height: 55px;
    color: var(--white-text); border-collapse: collapse;
  }
  .contacts td { padding: 0; white-space: nowrap; }
  .contacts .label { width: 160px; }
  .contacts .sep { width: 38px; }
  .brand-mark {
    position: absolute; left: 830px; top: 80px;
    display: flex; align-items: center; gap: 18px;
  }
  .brand-dot {
    width: 70px; height: 70px; border-radius: 50%;
    background: var(--plum);
  }
  .brand-name {
    font-size: 84px; font-weight: 600; color: var(--mark-ink);
    letter-spacing: 2px;
  }
</style>
</head>
<body>
  <div class="card">
    <svg class="card-waves" viewBox="0 0 1156 656" preserveAspectRatio="none" aria-hidden="true">
      <rect width="1156" height="656" fill="var(--lemon)"/>
      <path d="M590 0 C 760 120, 900 380, 880 656 L 0 656 L 0 0 Z" fill="var(--amber)" opacity="0.9"/>
      <path d="M585 0 C 720 120, 830 380, 790 656 L 0 656 L 0 0 Z" fill="var(--brown)" opacity="0.9"/>
      <path d="M575 0 C 690 130, 790 380, 700 656 L 0 656 L 0 0 Z" fill="var(--plum)"/>
    </svg>

    <div class="brand-mark">
      <span class="brand-dot"></span>
      <span class="brand-name">CHIA</span>
    </div>

    <div class="details">
      <h1 class="name">Dorian Pelkey</h1>
      <p class="role">Project Director</p>
      <p class="company">Continental Hoop Invitational</p>
      <div class="rule"></div>
      <p class="address">47 Marbury Lane, #06-11,<br>Singapore 915274</p>
      <table class="contacts">
        <tr><td class="label">Mob</td><td class="sep">:</td><td>+65 83147092</td></tr>
        <tr><td class="label">e-mail</td><td class="sep">:</td><td>dorian@hoopinvitational.net</td></tr>
        <tr><td class="label">Web</td><td class="sep">:</td><td>www.hoopinvitational.net</td></tr>
      </table>
    </div>
  </div>
</body>
</html>
```